Brightwire Hollow Business cards

one side I would like my logo (uploaded) and the other side I want my details. I'm an electrician in sydney. The logo side I'm happy with just a white background and our logo in the middle.

Details for other side
24/7 Sydney Electrician
Marcus Pell
0431 587 219
marcus@brightwirehollow.com.au
brightwirehollow.com.au
icons for facebook, instagram, linked in

Industry/Entity Type

electrician

Contact Information for Business Card

company info

```html
<!DOCTYPE html>
<html lang="en">
<head>
<meta charset="utf-8">
<title>Brightwire Hollow – Business Cards</title>
<link href="https://fonts.googleapis.com/css2?family=Montserrat:wght@500;700;800&display=swap" rel="stylesheet">
<style>
  :root {
    --backdrop: #c4c4c4;
    --card-dark: #1f1f1f;
    --card-light: #ffffff;
    --brand-red: #e8302a;
    --text-light: #ffffff;
    --divider: #8a2420;
  }
  * { margin: 0; padding: 0; box-sizing: border-box; }
  html, body {
    width: 1200px; height: 802px; overflow: hidden;
    background: var(--backdrop);
    font-family: "Montserrat", Arial, sans-serif;
  }
  .canvas {
    position: relative; width: 1200px; height: 802px;
    display: flex; align-items: center; justify-content: center; gap: 60px;
  }
  .card {
    width: 520px; height: 297px; border-radius: 18px;
    box-shadow: 0 14px 30px rgba(0,0,0,0.25);
    position: relative; overflow: hidden;
  }
  .card--details { background: var(--card-dark); display: flex; align-items: center; }
  .card--logo { background: var(--card-light); display: flex; align-items: center; justify-content: center; }

  .wordmark {
    display: flex; align-items: center; gap: 10px;
    color: var(--brand-red); font-weight: 800; text-transform: uppercase;
    line-height: 1;
  }
  .wordmark__dot { border-radius: 50%; background: var(--brand-red); flex: none; }
  .card--details .wordmark { font-size: 21px; width: 210px; padding-left: 28px; }
  .card--details .wordmark__dot { width: 14px; height: 14px; }
  .card--logo .wordmark { font-size: 38px; }
  .card--logo .wordmark__dot { width: 24px; height: 24px; }

  .divider { width: 1px; height: 150px; background: var(--divider); flex: none; }

  .details { padding-left: 24px; display: flex; flex-direction: column; }
  .details__name {
    color: var(--brand-red); font-weight: 800; font-size: 21px;
    text-transform: uppercase; letter-spacing: 0.5px; margin-bottom: 14px;
  }
  .details__list { list-style: none; }
  .details__item {
    display: flex; align-items: center; gap: 9px;
    color: var(--text-light); font-size: 12.5px; font-weight: 500;
    margin-bottom: 7px;
  }
  .details__item svg { width: 12px; height: 12px; fill: var(--brand-red); flex: none; }
  .social {
    display: flex; align-items: center; gap: 6px; margin-top: 24px;
    color: var(--text-light); font-size: 12px; font-weight: 700;
  }
  .social__label { margin-right: 4px; }
  .social__dot { width: 18px; height: 18px; border-radius: 50%; background: var(--brand-red); }
</style>
</head>
<body>
<main class="canvas">
  <section class="card card--details">
    <div class="wordmark"><span class="wordmark__dot"></span><span>Brightwire Hollow</span></div>
    <div class="divider"></div>
    <div class="details">
      <h1 class="details__name">Marcus Pell</h1>
      <ul class="details__list">
        <li class="details__item">
          <svg viewBox="0 0 24 24" aria-hidden="true"><path d="M6.6 10.8a15.1 15.1 0 0 0 6.6 6.6l2.2-2.2c.3-.3.7-.4 1-.2 1.1.4 2.3.6 3.6.6.6 0 1 .4 1 1V20c0 .6-.4 1-1 1A17 17 0 0 1 3 4c0-.6.4-1 1-1h3.5c.6 0 1 .4 1 1 0 1.3.2 2.5.6 3.6.1.3 0 .7-.2 1z"/></svg>
          0431 587 219
        </li>
        <li class="details__item">
          <svg viewBox="0 0 24 24" aria-hidden="true"><path d="M3 5h18v14H3zM4.5 6.5 12 12l7.5-5.5z" fill-rule="evenodd"/></svg>
          marcus@brightwirehollow.com.au
        </li>
        <li class="details__item">
          <svg viewBox="0 0 24 24" aria-hidden="true"><path d="M12 2a10 10 0 1 0 0 20 10 10 0 0 0 0-20zm-1 17.9A8 8 0 0 1 4.1 10H8v2l3 3zm6.9-2.5A2 2 0 0 0 16 16h-1v-3H9v-2h2V8h2V5.5a8 8 0 0 1 4.9 11.9z"/></svg>
          brightwirehollow.com.au
        </li>
        <li class="details__item">
          <svg viewBox="0 0 24 24" aria-hidden="true"><path d="M12 2a7 7 0 0 0-7 7c0 5.2 7 13 7 13s7-7.8 7-13a7 7 0 0 0-7-7zm0 9.5a2.5 2.5 0 1 1 0-5 2.5 2.5 0 0 1 0 5z"/></svg>
          24/7 Sydney Electrician
        </li>
      </ul>
      <div class="social">
        <span class="social__label">Follow Us :</span>
        <span class="social__dot"></span>
        <span class="social__dot"></span>
        <span class="social__dot"></span>
      </div>
    </div>
  </section>

  <section class="card card--logo">
    <div class="wordmark"><span class="wordmark__dot"></span><span>Brightwire Hollow</span></div>
  </section>
</main>
</body>
</html>
```